I need a website built for my organization.
We are the world's largest network of music producers.
The website should be professional, sharp, and high quality., We need a website built for The Halvern Sound Guild. We are one of the World's largest association of music producers.
The site must be professional, sharp, and high quality., I need a website built for my organization.
The site must be professional, sharp, and high quality.
Somewhere in the top half of the site there should be a form for the user to fill out. The details of the form are as follows:
Title (large and bold): Contact Us or Submit Your Music
Fields to include (* = required): First Name*, Last Name*, Age, Zip Code, Email Address*, Daytime Phone, Evening Phone, Comments
Then, there will be a "submit" button to proceed to next step of form. Just below the "submit" button, should be the following verbiage: "After submitting, you will have the opportunity to upload demos of your music (optional) and provide other pertinent information about yourself, band, or group."
Target Market(s)
Music producers and aspiring musicians
Industry/Entity Type
Group
Colors
Designer to choose colors to be used in the design.
Look and feel

```html
<!DOCTYPE html>
<html lang="en">
<head>
<meta charset="utf-8">
<title>The Halvern Sound Guild</title>
<link href="https://fonts.googleapis.com/css2?family=Arimo:wght@400;700&family=Marcellus&display=swap" rel="stylesheet">
<style>
:root{
  --page:#555556;
  --page-dark:#3c3c3d;
  --header:#4a4a4b;
  --nav:#2f2f30;
  --nav-line:#5c5c5d;
  --orange:#f26a1b;
  --gold:#e9a21d;
  --text:#f1f1f1;
  --muted:#c9c9c9;
  --footer:#3a3a3b;
  --panel-edge:#8a8a8a;
  --field:#efefef;
}
*{box-sizing:border-box;margin:0;padding:0}
html,body{width:1087px;height:1200px;overflow:hidden}
body{
  position:relative;
  font-family:"Arimo",Arial,sans-serif;
  color:var(--text);
  background:radial-gradient(ellipse at 50% 55%,#646465 0%,var(--page) 45%,var(--page-dark) 100%);
}
a{color:inherit;text-decoration:none}
.abs{position:absolute}

/* header */
.site-header{position:absolute;left:0;top:0;width:1087px;height:151px;
  background:linear-gradient(#585859,var(--header) 70%,#3e3e3f);}
.brand{left:150px;top:48px;display:flex;align-items:center;gap:12px}
.brand-mark{width:30px;height:30px;border-radius:50%;background:var(--orange)}
.brand-name{font-family:"Arimo",Arial,sans-serif;font-weight:700;font-size:28px;color:#e6e6e6;line-height:1.1;white-space:nowrap}
.search{left:638px;top:62px;width:163px;height:28px;border-radius:14px;
  background:linear-gradient(#f4f4f4,#cfcfcf);border:2px solid #9a9a9a;
  font-family:"Marcellus",serif;font-style:italic;font-size:13px;color:#8a8a8a;padding:4px 0 0 12px}
.search svg{position:absolute;right:10px;top:5px}
.live-chat{left:852px;top:13px;width:88px;height:30px;border-radius:6px;
  background:linear-gradient(#ffb23a,#e77a0e);border:2px solid #fff3c8;
  font-size:12px;font-weight:700;color:#4a2000;text-align:center;line-height:26px}
.social{left:832px;top:62px;display:flex;gap:8px}
.social span{width:22px;height:22px;border-radius:3px;background:#2f74c2;border:1px solid #cfe0f4}
.social span:nth-child(2){background:#e5781a}
.social span:nth-child(3){background:#3fa9dc}
.social span:nth-child(4){background:#2a6fa8}

.main-nav{left:367px;top:108px;width:577px;height:35px;border-radius:6px 6px 0 0;
  background:linear-gradient(#3a3a3b,var(--nav));display:flex;align-items:center;
  font-size:12px;font-weight:700;color:#f0f0f0}
.main-nav a{flex:none;white-space:nowrap;padding:0 18px;height:35px;line-height:35px;border-right:1px solid var(--nav-line)}
.main-nav a:last-child{border-right:0}
.main-nav .active{background:linear-gradient(#6d6d6e,#4f4f50);color:var(--orange);border-radius:4px 0 0 0}

/* hero */
.hero{left:0;top:151px;width:1087px;height:337px;
  background:linear-gradient(90deg,#3a1d08 0%,#2c3a30 18%,#4b5a50 40%,#3d4a42 60%,#2c3a30 82%,#3a1d08 100%)}
.hero-arrow{top:160px;width:0;height:0;border-top:10px solid transparent;border-bottom:10px solid transparent}
.hero-arrow.prev{left:36px;border-right:12px solid #3a9ad9}
.hero-arrow.next{right:36px;border-left:12px solid #3a9ad9}
.hero-thumb{left:433px;top:263px;width:221px;height:71px;border:3px solid #f2f2f2;
  background:linear-gradient(90deg,#3a2a14,#4d5b51,#3a2a14)}
.hero-pointer{left:536px;top:334px;border-left:8px solid transparent;border-right:8px solid transparent;border-top:8px solid #f2f2f2;width:0;height:0}
.dots{left:502px;top:506px;display:flex;gap:5px}
.dots span{width:12px;height:12px;border-radius:50%;background:#2a1a16}
.dots .on{background:var(--orange)}

/* submission form */
.submit-form{left:716px;top:162px;width:306px;padding:12px 14px 12px;
  background:rgba(28,28,29,.86);border:1px solid var(--panel-edge);border-radius:6px}
.form-title{font-size:20px;font-weight:700;color:#fff;margin-bottom:9px;white-space:nowrap}
.form-title span{color:var(--orange)}
.form-grid{display:grid;grid-template-columns:1fr 1fr;gap:6px}
.form-grid .wide{grid-column:span 2}
.form-grid input,.form-grid textarea{width:100%;height:24px;border:1px solid #9a9a9a;border-radius:3px;
  background:var(--field);font-family:"Arimo",Arial,sans-serif;font-size:11px;color:#333;padding:0 7px}
.form-grid input::placeholder,.form-grid textarea::placeholder{color:#6a6a6a}
.form-grid textarea{height:36px;padding-top:5px;resize:none}
.submit-btn{margin-top:8px;width:100%;height:26px;border:1px solid #ffd28a;border-radius:4px;
  background:linear-gradient(#ffa43a,#e2680e);font-family:"Arimo",Arial,sans-serif;font-size:12px;font-weight:700;color:#fff;text-transform:uppercase}
.form-note{margin-top:6px;font-size:9.5px;line-height:12.5px;color:var(--muted)}

/* welcome */
.section-title{font-family:"Marcellus",serif;font-size:23px;font-weight:400;color:#f4f4f4;display:flex;align-items:center;gap:10px}
.section-title em{font-style:italic;color:var(--orange)}
.title-icon{width:24px;height:24px;border-radius:3px;background:#d9d9d9}
.welcome-title{left:160px;top:542px}
.welcome-img{left:163px;top:589px;width:211px;height:122px;border:3px solid #777;border-radius:3px;
  background:radial-gradient(ellipse at 55% 50%,#3d6b1c,#1b2a12 45%,#050505 80%)}
.welcome-text{left:395px;top:591px;width:253px;font-size:10.5px;line-height:15.2px;color:#ececec}
.read-more{font-size:11.5px;color:var(--gold)}
.welcome-more{left:577px;top:702px}

.side-title{font-family:"Arimo",Arial,sans-serif;font-size:14px;font-weight:400;color:var(--orange);display:flex;align-items:center;gap:14px}
.side-title b{font-weight:400;color:#fff}
.side-icon{width:26px;height:24px;border-radius:3px;background:#2f8fd6}
.weblinks-title{left:688px;top:549px}
.weblinks{left:692px;top:593px;list-style:none;font-size:11px}
.weblinks li{height:29px;display:flex;align-items:center;gap:12px}
.weblinks li::before{content:"";width:0;height:0;border-top:4px solid transparent;border-bottom:4px solid transparent;border-left:6px solid var(--gold)}
.view-all{left:869px;top:699px}

/* tabs panel */
.tab-panel{left:148px;top:755px;width:506px;height:218px;border:1px solid var(--panel-edge);border-radius:6px;
  background:rgba(60,60,61,.55)}
.tabs{left:14px;top:12px;display:flex;align-items:flex-end;width:462px;border-bottom:1px solid #9a9a9a}
.tab-icon{width:22px;height:22px;border-radius:50%;background:var(--gold);margin-right:8px}
.tab{font-family:"Marcellus",serif;font-style:italic;font-size:12px;padding:0 10px 4px;text-transform:uppercase;white-space:nowrap}
.tab.active{color:var(--gold)}
.tab.plain{color:#fff;border:1px solid #9a9a9a;border-bottom:0;padding:3px 10px 4px}
.tab-img{left:21px;top:52px;width:100px;height:76px;border:2px solid #888;
  background:linear-gradient(#7a5a3a,#3a3a3c 40%,#6b6b6e)}
.tab-lead{left:136px;top:52px;width:358px;font-size:11px;font-weight:700;line-height:16px;color:#dadada}
.tab-lead p+p{margin-top:12px}
.tab-body{left:20px;top:138px;width:470px;font-size:10.5px;line-height:15px;color:#e0e0e0}
.tab-more{left:428px;top:197px}

.news-title{left:688px;top:767px}
.news{left:692px;top:804px;list-style:none}
.news li{height:43px;display:flex;gap:10px}
.news .cal{width:14px;height:14px;border-radius:2px;background:#f0f0f0;border-top:4px solid #d44;margin-top:3px}
.news .date{font-size:10px;color:var(--orange);display:block}
.news .what{font-size:10.5px;color:#f2f2f2}
.news-more{left:867px;top:948px}

/* footer */
.site-footer{left:0;top:991px;width:1087px;height:209px;background:linear-gradient(#3f3f40,var(--footer))}
.footer-col{top:12px}
.footer-col h3{font-size:13px;font-weight:400;color:var(--gold);margin-bottom:12px}
.footer-col li{list-style:none;font-size:10.5px;line-height:19px;color:#f0f0f0}
.follow li{display:flex;align-items:center;gap:10px;line-height:25px;font-size:11.5px}
.follow li span{width:17px;height:17px;border-radius:3px;background:#2f74c2}
.follow li:nth-child(2) span{background:#2a6fa8}
.follow li:nth-child(3) span{background:#3fa9dc}
.follow li:nth-child(4) span{background:#c8322a}
.footer-rule{left:0;top:163px;width:1087px;height:1px;background:#b77a12}
.copyright{left:0;top:178px;width:1087px;text-align:center;font-size:11px;color:#f0f0f0}
</style>
</head>
<body>

<header class="site-header">
  <div class="abs brand"><span class="brand-mark"></span><span class="brand-name">Halvern Sound Guild</span></div>
  <div class="abs live-chat">Live Chat</div>
  <div class="abs search">I'm looking for...
    <svg width="14" height="14" viewBox="0 0 14 14"><circle cx="6" cy="6" r="4.5" fill="none" stroke="#777" stroke-width="1.6"/><line x1="9.2" y1="9.2" x2="13" y2="13" stroke="#777" stroke-width="1.8"/></svg>
  </div>
  <div class="abs social" aria-label="Social links"><span></span><span></span><span></span><span></span></div>
  <nav class="abs main-nav">
    <a class="active" href="#">Home</a><a href="#">About HSG</a><a href="#">Membership</a><a href="#">News &amp; Events</a><a href="#">Resources</a><a href="#">Contact Us</a>
  </nav>
</header>

<section class="abs hero" role="img" aria-label="Rock band rehearsing in a studio, flanked by flaming electric guitar artwork">
  <span class="abs hero-arrow prev"></span>
  <span class="abs hero-arrow next"></span>
  <div class="abs hero-thumb" role="img" aria-label="Thumbnail of the band slide"></div>
  <span class="abs hero-pointer"></span>
</section>

<form class="abs submit-form" action="#">
  <h2 class="form-title">Submit Your <span>Music</span></h2>
  <div class="form-grid">
    <input type="text" placeholder="First Name*" required>
    <input type="text" placeholder="Last Name*" required>
    <input type="text" placeholder="Age">
    <input type="text" placeholder="Zip Code">
    <input class="wide" type="email" placeholder="Email Address*" required>
    <input type="tel" placeholder="Daytime Phone">
    <input type="tel" placeholder="Evening Phone">
    <textarea class="wide" placeholder="Comments"></textarea>
  </div>
  <button class="submit-btn" type="submit">Submit</button>
  <p class="form-note">After submitting, you will have the opportunity to upload demos of your music (optional) and provide other pertinent information about yourself, band, or group.</p>
</form>

<div class="abs dots"><span></span><span></span><span class="on"></span><span></span><span></span></div>

<h2 class="abs section-title welcome-title"><span class="title-icon"></span>Welcome To <em>HSG</em></h2>
<div class="abs welcome-img" role="img" aria-label="Abstract glowing music artwork"></div>
<p class="abs welcome-text">"Music can be your way of chilling out after an honest day's work , your refuge when the going gets tough; it might as well be your means to aspire for the divinity" – The Nadabrahma. Music universally has a tradition that has been derived from the ethno-cultural diversity that the land represents. It is rich in variety and pulsating with passion.</p>
<a class="abs read-more welcome-more" href="#">Read more...</a>

<h2 class="abs side-title weblinks-title"><span class="side-icon"></span><span>Weblinks <b>|</b> Partners</span></h2>
<ul class="abs weblinks">
  <li>HSG Copyright Board</li>
  <li>Performers Rights Society of HSG</li>
  <li>Music Copyright Society of HSG</li>
</ul>
<a class="abs read-more view-all" href="#">View All...</a>

<section class="abs tab-panel">
  <div class="abs tabs">
    <span class="tab-icon"></span>
    <span class="tab active">Music Producers</span>
    <span class="tab plain">Copyright Laws</span>
  </div>
  <div class="abs tab-img" role="img" aria-label="Recording studio mixing desk"></div>
  <div class="abs tab-lead">
    <p>Independent,Sole Traders &amp; Others Owning/Controlling rights in Recorded Music or Music Videos</p>
    <p>Rights of Authors, Composers and Publishers of Musical Works</p>
  </div>
  <p class="abs tab-body">Lorem ipsum dolor sit amet, consectetur adipisicing elit, sed do eiusmod tempor incididunt ut labore et dolore magna aliqua. Ut enim ad minim veniam, quis nostrud exercitation ullamco laboris nisi ut aliquip ex ea commodo consequat.</p>
  <a class="abs read-more tab-more" href="#">Read more...</a>
</section>

<h2 class="abs side-title news-title"><span class="side-icon" style="background:#4aa83a"></span><span>News <b>&amp;</b> Events</span></h2>
<ul class="abs news">
  <li><span class="cal"></span><div><span class="date">10/24/2010</span><span class="what">First Branch&nbsp; at Westmoor</span></div></li>
  <li><span class="cal"></span><div><span class="date">10/24/2012</span><span class="what">Second Branch&nbsp; at Eastgate</span></div></li>
  <li><span class="cal"></span><div><span class="date">10/24/2013</span><span class="what">Third Branch Opening Soon at Riverhill</span></div></li>
</ul>
<a class="abs read-more news-more" href="#">Read more...</a>

<footer class="abs site-footer">
  <div class="abs footer-col" style="left:174px"><h3>About Us</h3>
    <ul><li>Home</li><li>Resources</li><li>Art Gallery</li><li>News</li><li>Contactus</li></ul></div>
  <div class="abs footer-col" style="left:375px"><h3>Membership Information</h3>
    <ul><li>Membership Categories</li><li>Membership Application</li><li>Member Programs</li></ul></div>
  <div class="abs footer-col" style="left:576px"><h3>Contact Us</h3>
    <ul><li>HSG,</li><li>Near Corlow Field Park,</li><li>North Ashby Street,</li><li>Brennick, TX,</li><li>United States</li></ul></div>
  <div class="abs footer-col follow" style="left:769px"><h3>Follow Us On</h3>
    <ul><li><span></span>Socialwall</li><li><span></span>Proflink</li><li><span></span>Chirper</li><li><span></span>Vidstream</li></ul></div>
  <div class="abs footer-rule"></div>
  <p class="abs copyright">All Rights Reserved © 2013 halvernsound.net</p>
</footer>

</body>
</html>
```